MOLVT Study flyer

I need help designing a flyer for a research study that will include brain imaging in adolescents. The info is in the attached document. The study is called the Marrowby Orchard Lantern Vesper Trail (MOLVT) study. Ideally this would be returned as a document that I can edit in the future as we will have several new recruitment phases (different age groups, etc. I also would love to have a logo designed as part of this project, but I recognize that might be a separate design request.

```html
<!DOCTYPE html>
<html lang="en">
<head>
<meta charset="utf-8">
<title>MOLVT Study Flyer</title>
<link href="https://fonts.googleapis.com/css2?family=Outfit:wght@500;600;700;800&family=Poppins:wght@400;500&family=Lato:wght@400;700&display=swap" rel="stylesheet">
<style>
  :root {
    --navy: #202c5f;
    --navy-dark: #14204a;
    --yellow: #fcc419;
    --teal: #169c94;
    --purple: #5a3a9c;
    --sky: #12acea;
    --ink: #1f1f24;
    --rule: #b9b9bd;
    --pill: #9fd6ea;
    --paper: #ffffff;
    --cream: #fbf6e9;
  }
  * { margin: 0; padding: 0; box-sizing: border-box; }
  html, body { width: 950px; height: 1200px; overflow: hidden; background: var(--paper); }
  .flyer {
    position: relative; width: 950px; height: 1200px; overflow: hidden;
    background: linear-gradient(160deg, #ffffff 45%, var(--cream) 100%);
    font-family: "Lato", sans-serif; color: var(--ink);
  }
  .hero-band { position: absolute; left: 0; top: 0; }
  .headline {
    position: absolute; left: 52px; top: 96px;
    font-family: "Outfit", sans-serif; font-weight: 800;
    font-size: 58px; line-height: 66px; letter-spacing: -0.5px; color: #fff;
  }
  .headline .accent { color: var(--yellow); font-size: 62px; }
  .subhead {
    position: absolute; left: 62px; top: 298px;
    font-family: "Outfit", sans-serif; font-weight: 600;
    font-size: 26px; line-height: 30px; color: #fff;
  }
  .brand {
    position: absolute; left: 598px; top: 70px; display: flex; align-items: center; gap: 12px;
  }
  .brand-mark { width: 44px; height: 44px; background: var(--navy); }
  .brand-name {
    font-family: "Poppins", sans-serif; font-weight: 500; font-size: 21px; line-height: 24px; color: var(--navy);
  }
  .intro {
    position: absolute; left: 598px; top: 162px; width: 310px;
    font-family: "Poppins", sans-serif; font-size: 17px; line-height: 26px; color: var(--ink);
  }
  .photo {
    position: absolute; left: 508px; top: 440px; width: 442px; height: 760px;
    background: radial-gradient(ellipse at 55% 35%, #d9b79c 0%, #efe2c6 38%, #f5e98a 70%, #f4e48a 100%);
    border-radius: 220px 200px 0 0;
  }
  .sparkle { position: absolute; }
  .section-title {
    position: absolute; left: 73px; top: 472px;
    font-family: "Outfit", sans-serif; font-weight: 700; font-size: 23px; color: var(--purple);
  }
  .step { position: absolute; left: 79px; display: flex; gap: 23px; width: 430px; }
  .step-icon { flex: none; width: 56px; height: 56px; border-radius: 50%; display: flex; align-items: center; justify-content: center; }
  .step-text { font-size: 17px; line-height: 22px; padding-top: 0; }
  .step-text strong { font-weight: 700; }
  .icon-teal { background: var(--teal); }
  .icon-purple { background: var(--purple); }
  .icon-sky { background: var(--sky); }
  .divider { position: absolute; left: 87px; top: 809px; width: 400px; height: 1px; background: var(--rule); }
  .eligibility-title {
    position: absolute; left: 88px; top: 830px;
    font-family: "Outfit", sans-serif; font-weight: 700; font-size: 20px; color: var(--navy);
  }
  .eligibility-title span { color: var(--teal); }
  .criteria { position: absolute; left: 98px; top: 866px; list-style: none; width: 400px; }
  .criteria li {
    display: flex; gap: 10px; font-size: 16.5px; line-height: 20px; margin-bottom: 14px; color: var(--ink);
  }
  .criteria li svg { flex: none; margin-top: 3px; }
  .cta {
    position: absolute; left: 73px; top: 998px; width: 476px; height: 178px;
    border-radius: 12px; overflow: hidden; display: flex;
  }
  .cta-contact { position: relative; width: 300px; height: 100%; background: var(--navy); }
  .mail-badge {
    position: absolute; left: 26px; top: 27px; width: 88px; height: 88px; border-radius: 50%;
    background: #fff; display: flex; align-items: center; justify-content: center;
  }
  .cta-heading {
    position: absolute; left: 126px; top: 30px;
    font-family: "Outfit", sans-serif; font-weight: 700; font-size: 20px; line-height: 24px; color: var(--yellow);
  }
  .cta-note {
    position: absolute; left: 125px; top: 81px;
    font-family: "Poppins", sans-serif; font-size: 11.5px; line-height: 15px; color: #fff;
  }
  .cta-email {
    position: absolute; left: 26px; top: 135px; width: 261px; height: 28px; border-radius: 4px;
    background: var(--pill); color: var(--navy-dark);
    font-family: "Poppins", sans-serif; font-size: 15px; line-height: 28px; text-align: center;
  }
  .cta-reward {
    position: relative; flex: 1; background: var(--yellow); text-align: center; color: var(--navy-dark);
  }
  .gift-badge {
    position: absolute; left: 52px; top: 14px; width: 64px; height: 64px; border-radius: 50%;
    background: var(--navy-dark); display: flex; align-items: center; justify-content: center;
  }
  .reward-label {
    position: absolute; left: 0; right: 0; top: 84px;
    font-family: "Outfit", sans-serif; font-weight: 700; font-size: 16px; line-height: 18px;
  }
  .reward-amount {
    position: absolute; left: 0; right: 0; top: 114px;
    font-family: "Outfit", sans-serif; font-weight: 800; font-size: 52px; line-height: 56px; letter-spacing: -1px;
  }
</style>
</head>
<body>
<main class="flyer">
  <svg class="hero-band" width="560" height="450" viewBox="0 0 560 450" aria-hidden="true">
    <path d="M0 0 H556 V352 Q556 376 530 378 C420 384 340 405 250 432 C170 455 80 448 30 430 Q0 418 0 395 Z" fill="var(--navy)"/>
  </svg>

  <h1 class="headline">ARE YOU THE<br>PARENT OF A<br><span class="accent">CHILD AGE 10-17?</span></h1>
  <p class="subhead">DO THEY WORRY OR OVERTHINK<br>NEGATIVE EMOTIONS?</p>

  <div class="brand">
    <div class="brand-mark"></div>
    <div class="brand-name">Alderbrook<br>University</div>
  </div>

  <p class="intro">Alderbrook University researchers are seeking girls age 10-17 for a study about brain activity in emotions and decision-making and how they relate to puberty, anxiety and depression.</p>

  <div class="photo" role="img" aria-label="Photo of a thoughtful teenage girl in a yellow t-shirt looking upward, beneath a colourful illustrated brain"></div>

  <svg class="sparkle" style="left:881px;top:473px" width="18" height="18" viewBox="0 0 18 18" aria-hidden="true"><path d="M9 0V18M0 9H18" stroke="var(--yellow)" stroke-width="2"/></svg>
  <svg class="sparkle" style="left:542px;top:805px" width="18" height="18" viewBox="0 0 18 18" aria-hidden="true"><path d="M9 0V18M0 9H18" stroke="var(--yellow)" stroke-width="2"/></svg>

  <h2 class="section-title">STUDY PARTICIPATION INVOLVES:</h2>

  <div class="step" style="top:522px">
    <div class="step-icon icon-teal">
      <svg width="26" height="26" viewBox="0 0 26 26" fill="none" stroke="#fff" stroke-width="1.3"><rect x="5" y="9" width="16" height="11" rx="1"/><path d="M2 22H24"/><circle cx="13" cy="13" r="2"/><path d="M9.5 19c0-2 1.5-3 3.5-3s3.5 1 3.5 3"/><path d="M10 5a4 4 0 0 1 6 0M11.5 6.5a2 2 0 0 1 3 0"/></svg>
    </div>
    <p class="step-text"><strong>One one-hour interview</strong><br>(online or in-person) where your child<br>will discuss their thoughts</p>
  </div>

  <div class="step" style="top:612px">
    <div class="step-icon icon-purple">
      <svg width="24" height="26" viewBox="0 0 24 26" fill="none" stroke="#fff" stroke-width="1.2"><rect x="5" y="2" width="15" height="21"/><path d="M3 4V25H18"/><rect x="8" y="6" width="2" height="2"/><rect x="8" y="11" width="2" height="2"/><rect x="8" y="16" width="2" height="2"/><path d="M12 7H17M12 12H17M12 17H17"/></svg>
    </div>
    <p class="step-text"><strong>Online questionnaires</strong><br>(parent and child)</p>
  </div>

  <div class="step" style="top:681px">
    <div class="step-icon icon-sky" style="margin-top:14px">
      <svg width="30" height="30" viewBox="0 0 30 30" fill="none" stroke="#fff" stroke-width="1.4"><circle cx="15" cy="15" r="12"/><path d="M15 7V15L20 20"/></svg>
    </div>
    <p class="step-text"><strong>One two-hour visit</strong> where your child<br>will complete an MRI scan, answer<br>questions about their puberty stage,<br>and have a small hair sample taken to<br>study puberty hormones</p>
  </div>

  <div class="divider"></div>

  <h2 class="eligibility-title"><span>YOUR CHILD MAY</span> BE ELIGIBLE IF THEY:</h2>
  <ul class="criteria">
    <li><svg width="12" height="12" viewBox="0 0 12 12"><circle cx="6" cy="6" r="6" fill="var(--teal)"/><path d="M3.3 6.2L5.2 8L8.8 4.3" stroke="#fff" stroke-width="1.4" fill="none"/></svg>Are age 10-17</li>
    <li><svg width="12" height="12" viewBox="0 0 12 12"><circle cx="6" cy="6" r="6" fill="var(--teal)"/><path d="M3.3 6.2L5.2 8L8.8 4.3" stroke="#fff" stroke-width="1.4" fill="none"/></svg>Tend to worry or overthink negative thoughts</li>
    <li><svg width="12" height="12" viewBox="0 0 12 12"><circle cx="6" cy="6" r="6" fill="var(--teal)"/><path d="M3.3 6.2L5.2 8L8.8 4.3" stroke="#fff" stroke-width="1.4" fill="none"/></svg>Have not been diagnosed with psychosis,<br>learning problems, or autism</li>
  </ul>

  <section class="cta">
    <div class="cta-contact">
      <div class="mail-badge">
        <svg width="42" height="30" viewBox="0 0 42 30" fill="none" stroke="var(--ink)" stroke-width="2.4" stroke-linejoin="round"><rect x="2" y="2" width="38" height="26" rx="2"/><path d="M2 3L21 17L40 3M2 27L16 14M40 27L26 14"/></svg>
      </div>
      <h3 class="cta-heading">INTERESTED IN<br>PARTICIPATING?</h3>
      <p class="cta-note">Want more information?<br>Please contact us!</p>
      <div class="cta-email">molvtstudy@alderbrook.edu</div>
    </div>
    <div class="cta-reward">
      <div class="gift-badge">
        <svg width="30" height="30" viewBox="0 0 30 30" fill="none" stroke="#fff" stroke-width="1.4"><rect x="4" y="11" width="22" height="5"/><rect x="6" y="16" width="18" height="12"/><path d="M11 11V28M19 11V28"/><path d="M15 11C12 5 7 5 8 9C9 11 15 11 15 11C15 11 21 11 22 9C23 5 18 5 15 11Z"/></svg>
      </div>
      <p class="reward-label">COMPENSATION<br>UP TO</p>
      <p class="reward-amount">$140</p>
    </div>
  </section>
</main>
</body>
</html>
```